Vento Chiaro_4 Page Brochure (8-1/2"x 11)

Create a 4 -page brochure (8-1/2"x11 each page) in the exact likeness of the Silent auction piece. Instead of "bid to win" it will be " Redeem for a Complimentary"...Luxury Landscape Plan.
Expand brochure to show more/larger images of work./ description of services /portfolio (content can be duplicated from website)

```html
<!DOCTYPE html>
<html lang="en">
<head>
<meta charset="utf-8">
<title>Vento Chiaro – 4 Page Brochure</title>
<link rel="stylesheet" href="https://fonts.googleapis.com/css2?family=Cinzel:wght@400;700&family=Roboto:wght@400;700&display=swap">
<style>
:root{
  --stage:#e2e2e2;
  --forest:#3e6b4b;
  --forest-deep:#37613f;
  --lime:#b9d24a;
  --heading:#3f6d4a;
  --body:#555;
  --white:#fff;
}
*{margin:0;padding:0;box-sizing:border-box}
html,body{width:946px;height:1200px;overflow:hidden;background:var(--stage)}
body{position:relative;font-family:"Roboto",Arial,sans-serif}
.page{position:absolute;width:402px;height:520px;overflow:hidden;background:var(--white)}
.page--cover{left:50px;top:60px}
.page--services{left:495px;top:60px}
.page--portfolio{left:50px;top:628px;background:var(--forest)}
.page--thanks{left:495px;top:628px;background:var(--forest)}
.shapes{position:absolute;left:0;top:0;width:402px;height:520px}
.photo{position:absolute;border-radius:50%;overflow:hidden}

/* cover */
.brand{position:absolute;left:0;width:402px;top:26px;display:flex;justify-content:center;align-items:center;gap:8px}
.brand__dot{width:22px;height:22px;border-radius:50%;background:var(--lime)}
.brand__name{font-family:"Cinzel",serif;font-weight:400;font-size:22px;color:var(--heading)}
.cover__title{position:absolute;left:0;width:402px;top:92px;text-align:center;font-family:"Cinzel",serif;font-weight:400;font-size:19.5px;line-height:24px;color:var(--heading)}
.cover__intro{position:absolute;left:34px;width:334px;top:149px;text-align:center;font-size:7.9px;line-height:11.8px;color:var(--body)}
.contact{position:absolute;left:44px;color:var(--white);font-size:7.9px;line-height:11.8px;display:flex;gap:10px;align-items:flex-start}
.contact svg{width:14px;height:14px;flex:none}
.cover__footer{position:absolute;left:0;bottom:0;width:402px;height:25px;background:var(--forest-deep);color:var(--white);font-size:8px;letter-spacing:3px;text-align:center;line-height:25px}

/* services */
.services__title{position:absolute;left:0;width:402px;top:8px;text-align:center;font-family:"Cinzel",serif;font-size:18px;color:var(--white)}
.service__heading{position:absolute;font-weight:700;font-size:10.5px;color:var(--heading)}
.service__text{position:absolute;width:146px;font-size:5.3px;line-height:8.4px;color:var(--body);text-align:justify}

/* portfolio */
.portfolio__title{position:absolute;left:0;width:402px;top:20px;text-align:center;font-family:"Cinzel",serif;font-weight:700;font-size:20px;color:var(--white)}
.tile{position:absolute;width:103px;height:103px;border-radius:50%;border:1.5px solid var(--lime)}
.tile__label{position:absolute;width:120px;text-align:center;font-weight:700;font-size:10.3px;line-height:14px;color:var(--white)}

/* thanks */
.thanks__title{position:absolute;left:0;width:402px;top:80px;text-align:center;font-family:"Cinzel",serif;font-weight:700;font-size:28px;color:var(--white)}
.thanks__photo{position:absolute;left:74px;top:129px;width:254px;height:225px;border-radius:8px;background:linear-gradient(180deg,#4d86c4 0%,#7fb56a 45%,#5a8a3e 65%,#c9a874 100%)}
.badge{position:absolute;top:376px;height:43px;border:1.5px solid var(--white);border-radius:4px;opacity:.9}
</style>
</head>
<body>

<!-- Page 1: cover -->
<section class="page page--cover">
  <svg class="shapes" viewBox="0 0 402 520" aria-hidden="true">
    <path d="M302,0 C340,0 352,40 366,65 C380,88 390,96 402,100 L402,0 Z" fill="var(--forest)"/>
    <path d="M0,253 C22,292 70,336 170,340 L175,366 C90,362 30,332 0,292 Z" fill="var(--lime)"/>
    <path d="M0,292 C30,334 90,362 170,366 L300,366 C340,382 380,386 402,374 L402,520 L0,520 Z" fill="var(--forest)"/>
  </svg>
  <div class="brand"><span class="brand__dot"></span><span class="brand__name">Vento Chiaro</span></div>
  <h1 class="cover__title">Vento Chiaro Landscape<br>Design &amp; Construction</h1>
  <p class="cover__intro">Welcome to Vento Chiaro Landscape Design and Construction, where nature's beauty meets innovative design. Established in 1999, we stand as Denver's leading landscape design-build company, dedicated to crafting high-end residential spaces that redefine outdoor living.</p>
  <div class="photo" role="img" aria-label="Stone Mediterranean-style estate home with arched windows" style="left:54px;top:204px;width:122px;height:122px;background:linear-gradient(160deg,#6fa3d8 0%,#c9a27a 45%,#8a6a4a 75%,#4e7a3a 100%)"></div>
  <div class="photo" role="img" aria-label="Estate home set among red rock hills" style="left:180px;top:191px;width:66px;height:66px;background:linear-gradient(180deg,#b6855f 0%,#d8c0a0 55%,#6d7f4a 100%)"></div>
  <div class="photo" role="img" aria-label="Garden with wooden footbridge, river rock and pine shrubs" style="left:173px;top:267px;width:208px;height:208px;border:4px solid var(--white);background:radial-gradient(circle at 50% 55%,#8a6a48 0%,#5f7d3a 45%,#3f6a2e 80%,#8f8a82 100%)"></div>
  <div class="contact" style="top:385px">
    <svg viewBox="0 0 14 14" fill="none" stroke="#fff" stroke-width="1"><path d="M7 13 C3 8 2.5 6.5 2.5 5 A4.5 4.5 0 0 1 11.5 5 C11.5 6.5 11 8 7 13 Z"/><circle cx="7" cy="5" r="1.6"/></svg>
    <span>4150 Alder Ridge Ct.<br>Suite 210 Lakeview,<br>Colorado 80231</span>
  </div>
  <div class="contact" style="top:436px">
    <svg viewBox="0 0 14 14" fill="none" stroke="#fff" stroke-width="1"><rect x="1" y="3" width="12" height="8"/><path d="M1 3 L7 8 L13 3"/></svg>
    <span>hello@ventochiaroco.com</span>
  </div>
  <div class="contact" style="top:460px">
    <svg viewBox="0 0 14 14" fill="none" stroke="#fff" stroke-width="1"><path d="M3 1.5 L5 1.5 L6 4.5 L4.5 5.5 C5.3 7.3 6.7 8.7 8.5 9.5 L9.5 8 L12.5 9 L12.5 11 C12.5 12 11.5 12.8 10.5 12.5 C6 11.5 2.5 8 1.5 3.5 C1.3 2.5 2 1.5 3 1.5 Z"/></svg>
    <span>(303) 555-0147</span>
  </div>
  <div class="cover__footer">WWW.VENTOCHIAROCO.COM</div>
</section>

<!-- Page 2: services -->
<section class="page page--services">
  <svg class="shapes" viewBox="0 0 402 520" aria-hidden="true">
    <ellipse cx="200" cy="0" rx="102" ry="56" fill="var(--forest)"/>
    <circle cx="297" cy="131" r="69" fill="var(--lime)"/>
    <circle cx="104" cy="258" r="72" fill="var(--lime)"/>
    <circle cx="298" cy="406" r="68" fill="var(--lime)"/>
    <path d="M0,520 L0,490 C40,468 80,468 130,474 C220,485 300,470 402,434 L402,520 Z" fill="var(--lime)"/>
    <path d="M0,520 L0,496 C30,478 70,474 110,479 C200,494 290,506 402,470 L402,520 Z" fill="var(--forest)"/>
  </svg>
  <h2 class="services__title">Our Services</h2>
  <h3 class="service__heading" style="left:50px;top:73px">Consultation</h3>
  <p class="service__text" style="left:50px;top:91px">At Vento Chiaro our journey begins with an immersive consultation tailored to your unique aspirations. Our seasoned team of landscape architects and designers will personally engage with you to understand your lifestyle, preferences, and dreams. This initial phase is not just a meeting; it's a creative collaboration, where we blend your vision with our expertise to conceptualize an outdoor masterpiece. From the first handshake, expect a seamless process that prioritizes your desires, ensuring a truly bespoke experience.</p>
  <div class="photo" role="img" aria-label="Designer reviewing plans with a homeowner on a porch" style="left:223px;top:58px;width:130px;height:130px;background:linear-gradient(150deg,#d9d3c4 0%,#b8c9de 45%,#6f8fb8 75%,#c9b59a 100%)"></div>
  <div class="photo" role="img" aria-label="Colored landscape site plan with patio, pergola and pool" style="left:38px;top:181px;width:142px;height:142px;background:radial-gradient(circle at 40% 50%,#d8c39a 0%,#c9b07e 50%,#7aa05a 75%,#2f6fc9 100%)"></div>
  <h3 class="service__heading" style="left:207px;top:209px">Landscape Design</h3>
  <p class="service__text" style="left:207px;top:227px">With your vision firmly in our grasp, our skilled designers meticulously craft a breathtaking landscape design that captures the essence of luxury living. Every detail, from the placement of exquisite flora to the selection of premium materials, is curated to elevate your outdoor space to unparalleled heights. Immerse yourself in a world where aesthetics and functionality harmonize seamlessly. Our commitment to excellence ensures that your personalized design not only reflects your style but enhances the beauty of your residence.</p>
  <h3 class="service__heading" style="left:50px;top:337px">Construction</h3>
  <p class="service__text" style="left:50px;top:355px">As the sun sets on the design phase, the construction journey begins, transforming your dreams into a tangible masterpiece. Our seasoned craftsmen, selected for their unwavering dedication to precision, meticulously bring the design to life. Impeccable stonework, lush greenery, and bespoke water features materialize under the skillful hands of our artisans. The construction phase is not just about building; it's about sculpting an outdoor sanctuary that mirrors the opulence of your lifestyle. Rest assured, our commitment to excellence ensures that the final result will surpass even the loftiest expectations.</p>
  <div class="photo" role="img" aria-label="Lit poolside cabana at night reflected in the pool" style="left:223px;top:332px;width:130px;height:130px;background:linear-gradient(180deg,#2a2430 0%,#e0a070 40%,#8a4a8a 65%,#4a2a9a 100%)"></div>
</section>

<!-- Page 3: portfolio -->
<section class="page page--portfolio">
  <svg class="shapes" viewBox="0 0 402 520" aria-hidden="true">
    <path d="M0,385 C20,432 60,480 200,500 C260,508 295,514 302,520 L0,520 Z" fill="var(--lime)"/>
  </svg>
  <h2 class="portfolio__title">OUR PORTFOLIO</h2>

  <div class="tile photo" role="img" aria-label="Porch garden with red flower beds" style="left:32px;top:46px;background:linear-gradient(180deg,#e8e4dc 0%,#6a9a4a 50%,#d0283a 80%,#4a7a2a 100%)"></div>
  <div class="tile__label" style="left:24px;top:151px">Landscaping</div>
  <div class="tile photo" role="img" aria-label="Stone patio bar with red cushioned seating" style="left:149px;top:67px;background:linear-gradient(180deg,#4a6a3a 0%,#c98a5a 45%,#c83030 75%,#8a6a50 100%)"></div>
  <div class="tile__label" style="left:141px;top:171px">Hardscaping</div>
  <div class="tile photo" role="img" aria-label="Evening outdoor dining table under string lights" style="left:266px;top:87px;background:radial-gradient(circle at 50% 60%,#d88a3a 0%,#6a4a30 50%,#2a2420 100%)"></div>
  <div class="tile__label" style="left:258px;top:192px">Outdoor Living</div>

  <div class="tile photo" role="img" aria-label="Patio seating beside a brick fireplace" style="left:32px;top:182px;background:linear-gradient(160deg,#8a5a4a 0%,#9a9590 50%,#5a5550 100%)"></div>
  <div class="tile__label" style="left:24px;top:287px">Outdoor Dining</div>
  <div class="tile photo" role="img" aria-label="Outdoor kitchen with grill at dusk above mountains" style="left:149px;top:202px;background:linear-gradient(180deg,#e89a6a 0%,#3a3a4a 35%,#c98a4a 65%,#7a5a3a 100%)"></div>
  <div class="tile__label" style="left:141px;top:307px">Outdoor Kitchens</div>
  <div class="tile photo" role="img" aria-label="Lit pool and cabana at night" style="left:266px;top:223px;background:linear-gradient(180deg,#3a2a2a 0%,#e0a070 40%,#3a4ad0 65%,#9a5ad0 100%)"></div>
  <div class="tile__label" style="left:258px;top:328px">Pools &amp; Spas<br>Water Features</div>

  <div class="tile photo" role="img" aria-label="Fire feature overlooking a mountain valley" style="left:32px;top:313px;background:linear-gradient(180deg,#dcd0c0 0%,#4a5a4a 40%,#f07a20 65%,#6a5a4a 100%)"></div>
  <div class="tile__label" style="left:24px;top:418px">Fireplaces &amp;<br>Firepits</div>
  <div class="tile photo" role="img" aria-label="Garden structure with planters and lighting" style="left:149px;top:334px;background:linear-gradient(180deg,#5a8a4a 0%,#7a9a5a 40%,#b07a4a 75%,#8a6040 100%)"></div>
  <div class="tile__label" style="left:141px;top:439px">Garden Structures</div>
  <div class="tile photo" role="img" aria-label="Stone pavilion framing a mountain view" style="left:266px;top:370px;background:linear-gradient(180deg,#6a3a2a 0%,#7a8ab0 35%,#5a6a5a 60%,#b0a090 100%)"></div>
  <div class="tile__label" style="left:258px;top:474px">Masonry</div>
</section>

<!-- Page 4: thank you -->
<section class="page page--thanks">
  <svg class="shapes" viewBox="0 0 402 520" aria-hidden="true">
    <circle cx="101" cy="167" r="61" fill="var(--lime)"/>
    <path d="M0,383 C20,432 60,480 200,500 C260,508 295,514 303,520 L0,520 Z" fill="var(--lime)"/>
  </svg>
  <h2 class="thanks__title">THANK YOU</h2>
  <div class="thanks__photo" role="img" aria-label="Flagstone garden patio with iron gate, flowering shrubs and lawn"></div>
  <div class="badge" style="left:97px;width:98px"></div>
  <div class="badge" style="left:224px;width:83px"></div>
</section>

</body>
</html>
```